RTV ELECTRICAL GROUP Website Providing Electrical Services

We're a company providing electrical services to the public. We're located in Bankstown a suburb in Sydney, Australia. We are a team of 4 electricians that provide service work to the public. We work on new construction buildings such as single story, double story & units. We also do office fit outs & commercial factory work.

Target Market(s)

All Age Groups
Construction People
Sydney, Australia

Industry/Entity Type

Electrical

Contact Information for Business Card

Name Gavin Lorrimer
Contact Number 0481 502 743
Company License 904517B
ABN 53 204 871 365
Residential Commercial Industrial
info@rtvelectrical.example.com.au

Coding

Coded - Design and coding required

Number of Pages Required

5+ page

Font styles to use
Serif
Sans Serif

Colors

Designer to choose colors to be used in the design.

Requirements
Must have
• WORDPRESS
• Nice & Simple
• Eye catching
• Easy to Read
• Contact details
• Instagram Linked
• Facebook Page Linked
• All Social Media Linked
• Live Chat
• Form Submission
• Testimonial
• Specify services Offered
• About Us (Company details)
• Industrial Installation Page
• Residential Installation Page
• Commercial Installation Page
• Mode of payment (cash, credit-debit card, cheque)
• Local & national electrical news
• Project Videos
• Newsletter
• Level 2 licensed accredited
• Project pictures and articles
• Awards
• Legalities (company's policy, terms, rules)
• FAQ's (Frequently asked questions)
• Collaboration Projects
• Careers
• Projects
• Suppliers
• Customer Perks (discounts or freebies)
• Employees Informations (pictures and basic information)
• Opening Hours and Map location
• Company Logo & Company License (owner license)
• Accreditation
• Customer Service
• Safety/Safety tips
• Clients information (regular clients)
• Expertise
• Company's processes
• Timeline page
• Homepage
• Specify installations
• Search toolbar
• Portfolio
• Request for an appointment - servicing
• Feedbacks
Nice to have
• Articles (better if recent project articles)
• Advertisement
• Influencer Quote
• Sneak Peeks (if you have new services offered)
• Staff Highlights
• Job Hiring (Career Growth)
• Ratings (Rate our service)
• A day/week in the work
• Personal Anecdotes
• Before and after post projects
• Ecological Values
• Marketing feature
• Tagline
• Streaming interactive videos
• Timeline
• Calendar
• Blog
• Emergency Services/Hotline
• Additional services offered
• Transportation (vehicle - car images of our company)
• Comment box (company - clients)
• Rate Us (Performance rating)
Should not have
• Website shouldn't be dark
• Website shouldn't be hard to read
• Advertisement of competitors
• Moving objects
• Dark background

```html
<!DOCTYPE html>
<html lang="en">
<head>
<meta charset="utf-8">
<title>RTV Electrical Group</title>
<link href="https://fonts.googleapis.com/css2?family=Montserrat:wght@400;500;600;700&family=Open+Sans:wght@400;600;700&display=swap" rel="stylesheet">
<style>
:root{
  --blue:#1c5f8c;
  --blue-deep:#14496d;
  --ink:#1f1f1f;
  --text:#444;
  --muted:#777;
  --line:#d9d9d9;
  --panel:#f3f3f3;
  --dark-btn:#3b3b3b;
  --footer:#333333;
  --footer-text:#d8d8d8;
  --white:#ffffff;
  --star:#f2b01e;
}
*{box-sizing:border-box;margin:0;padding:0}
html,body{width:1200px;height:4500px;overflow:hidden;background:var(--white)}
body{font-family:"Open Sans",Arial,sans-serif;color:var(--text)}
.page{position:relative;width:1200px;height:4500px;overflow:hidden}
.abs{position:absolute}
h1,h2,h3,h4{font-family:"Montserrat",Arial,sans-serif;color:var(--ink)}
.btn{position:absolute;display:flex;align-items:center;justify-content:center;font-family:"Montserrat",Arial,sans-serif;font-weight:700;font-size:16px;color:var(--white);background:var(--blue);border-radius:5px}
.btn.dark{background:var(--dark-btn)}
.photo{position:absolute}

/* header */
.site-header{position:absolute;left:0;top:0;width:1200px;height:144px;background:var(--white)}
.brand{position:absolute;left:100px;top:48px;display:flex;align-items:center;gap:14px}
.brand-dot{width:40px;height:40px;border-radius:50%;background:var(--blue)}
.brand-name{font-family:"Montserrat",Arial,sans-serif;font-weight:600;font-size:19px;color:var(--blue);line-height:1.15;width:160px}
.main-nav{position:absolute;left:470px;top:84px;display:flex;gap:34px;font-family:"Montserrat",Arial,sans-serif;font-size:16px;font-weight:500;color:var(--ink)}
.main-nav .active{color:var(--blue);font-weight:700;border-bottom:3px solid var(--blue);padding-bottom:14px}
.top-contact{position:absolute;top:32px;display:flex;gap:10px;align-items:flex-start;font-size:13px;line-height:1.3;color:var(--ink)}
.top-contact .ico{width:26px;height:26px;border-radius:50%;background:var(--blue);flex:none}
.top-contact b{color:var(--blue)}

/* hero */
.hero{position:absolute;left:0;top:144px;width:1200px;height:582px;background:linear-gradient(100deg,#c9b990 0%,#7d7566 30%,#4c4a44 60%,#2e2d2a 100%)}
.hero-copy{position:absolute;left:300px;top:428px;width:520px;text-align:center;color:var(--white)}
.hero-copy h1{color:var(--white);font-size:23px;font-weight:600;white-space:nowrap}
.hero-copy p{font-size:15px;font-weight:600;margin-top:6px}
.quote-form{position:absolute;left:855px;top:310px;width:225px;height:294px;background:rgba(30,30,30,.85);padding:20px 12px}
.quote-form h4{color:var(--white);font-size:16px;text-align:center;letter-spacing:1px;margin-bottom:16px}
.field{height:34px;border:1px solid #6d6d6d;background:#262626;color:#dcdcdc;font-size:13px;padding:8px;margin-bottom:10px}
.field.tall{height:62px}
.quote-form .send{height:34px;background:var(--blue);color:var(--white);font-weight:700;font-size:14px;display:flex;align-items:center;justify-content:center;border-radius:3px}
.slider-dots{position:absolute;left:576px;top:750px;display:flex;gap:8px}
.slider-dots span{width:8px;height:8px;border-radius:50%;background:#333}

/* section heads */
.section-title{position:absolute;left:0;width:1200px;text-align:center;font-size:25px;font-weight:600}
.section-sub{position:absolute;left:0;width:1200px;text-align:center;font-size:15px;color:var(--ink);font-weight:600;line-height:1.4}
.divider{position:absolute;left:570px;width:60px;height:14px}

/* services */
.service{position:absolute;width:270px;text-align:center}
.service svg{display:block;margin:0 auto 10px}
.service h3{font-size:17px;font-weight:700;text-transform:uppercase;margin-bottom:6px}
.service p{font-size:14px;font-weight:600;color:var(--ink);line-height:1.35}

/* gallery */
.gallery-band{position:absolute;left:0;top:1515px;width:1200px;height:696px;background:var(--blue)}
.filters{position:absolute;left:0;top:1630px;width:1200px;text-align:center;font-family:"Montserrat",Arial,sans-serif;font-size:13px;font-weight:600;color:var(--white);letter-spacing:.5px}
.filters span{margin:0 8px}

/* testimonials */
.quote-card{position:absolute;left:705px;top:2460px;width:250px;text-align:center}
.quote-card h4{font-size:17px;font-weight:500;letter-spacing:.5px}
.quote-card .role{color:var(--blue);font-weight:700;font-size:14px;margin:4px 0 12px}
.quote-card p{font-size:13.5px;line-height:1.4;color:var(--text)}
.stars{color:var(--star);font-size:16px;margin-top:8px;letter-spacing:2px}

/* benefits */
.benefits-band{position:absolute;left:0;top:2895px;width:600px;height:276px;background:var(--blue)}
.benefits-copy{position:absolute;left:118px;top:2935px;width:450px;color:var(--white)}
.benefits-copy h2{color:var(--white);font-size:28px;font-weight:600;letter-spacing:.5px}
.benefits-copy h3{color:var(--white);font-size:17px;font-weight:600;margin:4px 0 16px}
.benefits-copy p{font-size:14px;font-weight:600;line-height:1.4;margin-bottom:12px}

/* blog */
.post{position:absolute;top:3399px;width:316px;height:342px;background:var(--panel)}
.post .thumb{position:relative;width:300px;height:200px;margin:8px 8px 0}
.post .date-badge{position:absolute;left:0;top:0;width:38px;height:38px;background:var(--blue);color:var(--white);font-size:11px;font-weight:700;text-align:center;line-height:1.2;padding-top:5px}
.post h4{font-size:14px;font-weight:700;color:var(--blue);margin:10px 12px 4px;text-transform:uppercase}
.post .meta{font-size:12px;color:var(--muted);margin:0 12px 10px;display:flex;gap:14px}
.post p{font-size:13.5px;color:var(--text);margin:0 12px;line-height:1.4}
.post .more{font-size:13.5px;color:var(--text);margin:8px 12px}

/* newsletter */
.news-input{position:absolute;left:294px;top:3978px;width:432px;height:36px;border:1px solid #bbb;font-size:13px;padding:9px 12px;color:var(--muted)}
.news-btn{left:726px;top:3978px;width:150px;height:36px;font-size:14px;border-radius:0 5px 5px 0}

/* footer */
.site-footer{position:absolute;left:0;top:4110px;width:1200px;height:330px;background:var(--footer);color:var(--footer-text)}
.footer-col{position:absolute;top:68px;font-size:14px;line-height:1.6}
.footer-col h4{color:var(--white);font-size:14px;font-weight:700;letter-spacing:.5px;margin-bottom:20px}
.footer-col li{list-style:none}
.footer-col li::before{content:"\203A";margin-right:10px}
.addr-row{display:flex;gap:10px;margin-bottom:6px}
.addr-row .pin{width:14px;height:14px;border-radius:50%;background:var(--white);flex:none;margin-top:4px}
.mini-field{border:1px solid #555;background:#2a2a2a;height:30px;font-size:12px;padding:6px 8px;color:#ccc}
.social{display:flex;gap:12px;margin-top:16px}
.social span{width:22px;height:22px;border-radius:50%;background:var(--white)}
.copyright{position:absolute;left:0;top:4440px;width:1200px;height:60px;background:var(--blue);color:var(--white);font-size:14px;font-weight:600;padding:20px 115px}
.live-chat{position:absolute;left:930px;top:4430px;width:218px;height:50px;background:#1f6fb3;border-radius:8px 8px 0 0;color:var(--white);font-family:"Montserrat",Arial,sans-serif;font-weight:700;font-size:22px;display:flex;align-items:center;justify-content:center;gap:12px}
.live-chat i{width:26px;height:22px;background:var(--white);border-radius:6px;display:block}
</style>
</head>
<body>
<div class="page">

  <header class="site-header">
    <div class="brand">
      <div class="brand-dot"></div>
      <div class="brand-name">RTV ELECTRICAL GROUP</div>
    </div>
    <nav class="main-nav">
      <span class="active">HOME</span><span>ABOUT US</span><span>SERVICES</span><span>PROJECT GALLERY</span><span>BLOG</span><span>CONTACT</span>
    </nav>
    <div class="top-contact" style="left:790px">
      <div class="ico"></div><div>100 Example Street<br>Sydney, NSW</div>
    </div>
    <div class="top-contact" style="left:975px">
      <div class="ico"></div><div><b>CALL US NOW</b><br>0491 570 156</div>
    </div>
  </header>

  <section class="hero" role="img" aria-label="Photo of an electrician wearing a hard hat wiring a switchboard"></section>
  <div class="hero-copy">
    <h1>Electrical Company Providing Services</h1>
    <p>Lorem Ipsum is simply Dummy Text of The Printing .</p>
  </div>
  <div class="btn" style="left:510px;top:519px;width:132px;height:36px">Read More</div>
  <form class="quote-form">
    <h4>GET A QUOTE</h4>
    <div class="field">Name</div>
    <div class="field">Email</div>
    <div class="field">Phone</div>
    <div class="field tall">Message</div>
    <div class="send">Submit</div>
  </form>
  <div class="slider-dots"><span></span><span></span><span></span></div>

  <!-- services -->
  <h2 class="section-title" style="top:785px">Our Services</h2>
  <svg class="divider" style="top:820px" viewBox="0 0 60 14"><line x1="0" y1="7" x2="22" y2="7" stroke="#1c5f8c" stroke-width="1.5"/><line x1="38" y1="7" x2="60" y2="7" stroke="#1c5f8c" stroke-width="1.5"/><path d="M27 2 L33 7 L28 8 L33 12" fill="none" stroke="#1c5f8c" stroke-width="1.5"/></svg>
  <p class="section-sub" style="top:838px;left:390px;width:420px">Lorem Ipsum is simply dummy text of the printing and typesetting industry.</p>

  <div class="service" style="left:130px;top:890px">
    <svg width="56" height="60" viewBox="0 0 56 60"><rect x="14" y="6" width="6" height="52" fill="#1c5f8c"/><rect x="4" y="6" width="48" height="5" fill="#1c5f8c"/><line x1="44" y1="11" x2="44" y2="28" stroke="#1c5f8c" stroke-width="2"/><rect x="38" y="28" width="12" height="8" fill="#1c5f8c"/><rect x="6" y="54" width="24" height="5" fill="#1c5f8c"/></svg>
    <h3>Construction Buildings</h3>
    <p>Lorem Ipsum Is Simply Dummy and of The Printing And Industry.</p>
  </div>
  <div class="service" style="left:130px;top:1060px">
    <svg width="60" height="56" viewBox="0 0 60 56"><rect x="8" y="4" width="44" height="28" fill="none" stroke="#1c5f8c" stroke-width="4"/><rect x="4" y="40" width="52" height="5" fill="#1c5f8c"/><rect x="10" y="45" width="5" height="10" fill="#1c5f8c"/><rect x="45" y="45" width="5" height="10" fill="#1c5f8c"/></svg>
    <h3>Office Fit Outs</h3>
    <p>Lorem Ipsum Is Simply Dummy and of The Printing And Industry.</p>
  </div>
  <div class="service" style="left:130px;top:1240px">
    <svg width="50" height="60" viewBox="0 0 50 60"><rect x="8" y="4" width="34" height="54" fill="#1c5f8c"/><g fill="#fff"><rect x="14" y="10" width="7" height="7"/><rect x="29" y="10" width="7" height="7"/><rect x="14" y="24" width="7" height="7"/><rect x="29" y="24" width="7" height="7"/><rect x="14" y="38" width="7" height="7"/><rect x="29" y="38" width="7" height="7"/></g></svg>
    <h3>Commercial Factory</h3>
    <p>Lorem Ipsum Is Simply Dummy and of The Printing And Industry.</p>
  </div>

  <div class="photo" style="left:480px;top:900px;width:195px;height:456px;background:linear-gradient(180deg,#f1c232 0%,#e8d9b5 14%,#5d6670 30%,#4f5760 62%,#a0702e 66%,#2f3640 100%);border-radius:40px 40px 10px 10px" role="img" aria-label="Illustration of an electrician in a hard hat and tool belt with arms crossed"></div>

  <div class="service" style="left:730px;top:890px">
    <svg width="50" height="60" viewBox="0 0 50 60"><path d="M25 4 L46 20 V58 H4 V20 Z" fill="#1c5f8c"/><g fill="#fff"><rect x="12" y="26" width="10" height="9"/><rect x="28" y="26" width="10" height="9"/><rect x="12" y="42" width="10" height="9"/><rect x="28" y="42" width="10" height="16"/></g></svg>
    <h3>Double Story</h3>
    <p>Lorem Ipsum Is Simply Dummy and of The Printing And Industry.</p>
  </div>
  <div class="service" style="left:730px;top:1075px">
    <svg width="56" height="56" viewBox="0 0 56 56"><rect x="18" y="16" width="22" height="22" rx="4" transform="rotate(-45 29 27)" fill="#1c5f8c"/><line x1="34" y1="10" x2="42" y2="2" stroke="#1c5f8c" stroke-width="4"/><line x1="44" y1="20" x2="52" y2="12" stroke="#1c5f8c" stroke-width="4"/><path d="M18 38 L6 50" stroke="#1c5f8c" stroke-width="4"/></svg>
    <h3>Installations</h3>
    <p>Lorem Ipsum Is Simply Dummy and of The Printing And Industry.</p>
  </div>
  <div class="service" style="left:730px;top:1245px">
    <svg width="56" height="52" viewBox="0 0 56 52"><path d="M28 2 L54 24 H46 V50 H10 V24 H2 Z" fill="#1c5f8c"/><rect x="23" y="32" width="10" height="18" fill="#fff"/></svg>
    <h3>Single Story</h3>
    <p>Lorem Ipsum Is Simply Dummy and of The Printing And Industry.</p>
  </div>

  <div class="btn" style="left:510px;top:1416px;width:165px;height:36px">View More</div>

  <!-- gallery -->
  <section class="gallery-band"></section>
  <h2 class="section-title" style="top:1547px;color:var(--white)">PROJECT GALLERY</h2>
  <svg class="divider" style="top:1584px" viewBox="0 0 60 14"><line x1="0" y1="7" x2="22" y2="7" stroke="#fff" stroke-width="1.5"/><line x1="38" y1="7" x2="60" y2="7" stroke="#fff" stroke-width="1.5"/><path d="M27 2 L33 7 L28 8 L33 12" fill="none" stroke="#fff" stroke-width="1.5"/></svg>
  <div class="filters"><span>ALL</span>|<span>HOUSE</span>|<span>DOUBLE STORY</span>|<span>OFFICE</span>|<span>COMMERCIAL FACTORY</span>|<span>OTHER</span></div>

  <div class="photo" style="left:120px;top:1674px;width:234px;height:198px;background:linear-gradient(135deg,#c9ccd2,#4b86c2 55%,#d1a178)" role="img" aria-label="Hands stripping coloured wires"></div>
  <div class="photo" style="left:363px;top:1674px;width:228px;height:198px;background:linear-gradient(160deg,#b8c2c9,#5f7385 60%,#3b4a57)" role="img" aria-label="Office interior with switchboard panels"></div>
  <div class="photo" style="left:606px;top:1674px;width:228px;height:198px;background:linear-gradient(160deg,#dfe5ea,#7f8d97 50%,#3c4650)" role="img" aria-label="Modern commercial building exterior"></div>
  <div class="photo" style="left:849px;top:1674px;width:225px;height:198px;background:linear-gradient(160deg,#e5e7e8,#a1a6a8 55%,#5a5f61)" role="img" aria-label="Double storey house exterior"></div>
  <div class="photo" style="left:120px;top:1887px;width:234px;height:198px;background:linear-gradient(180deg,#e2e4e6,#9aa0a6 55%,#4c5257)" role="img" aria-label="Open plan office with desks"></div>
  <div class="photo" style="left:363px;top:1887px;width:228px;height:198px;background:linear-gradient(180deg,#d9d2c3,#8a7d68 60%,#4b4438)" role="img" aria-label="Office fit out with workstations"></div>
  <div class="photo" style="left:606px;top:1887px;width:228px;height:198px;background:linear-gradient(135deg,#f0f0f0,#d8c24a 35%,#3d7fc1 70%,#e6e6e6)" role="img" aria-label="Circuit breakers with coloured wiring"></div>
  <div class="photo" style="left:849px;top:1887px;width:225px;height:198px;background:linear-gradient(135deg,#f1d35a,#3e5a86 45%,#c9cdd2)" role="img" aria-label="Electrician in hard hat working on a panel"></div>

  <div class="btn dark" style="left:510px;top:2127px;width:165px;height:34px">View More</div>

  <!-- testimonials -->
  <h2 class="section-title" style="top:2303px;font-size:21px">TESTIMONIALS</h2>
  <p class="section-sub" style="top:2338px;font-weight:400;font-size:14px">Lorem Ipsum is simply dummy text of the printing industry.</p>
  <div class="photo" style="left:201px;top:2379px;width:393px;height:297px;background:linear-gradient(160deg,#e6e8ea,#9ea6ad 45%,#4c5660)" role="img" aria-label="Team working at computers in an office"></div>
  <div class="photo" style="left:525px;top:2460px;width:150px;height:150px;border-radius:50%;background:linear-gradient(160deg,#d8cfc4,#8b7b6b);border:6px solid #fff" role="img" aria-label="Portrait of the client giving the testimonial"></div>
  <div class="quote-card">
    <h4>MARCUS DELANEY</h4>
    <div class="role">Creative Director</div>
    <p>Lorem Ipsum simply dummy text the printing and typesetting industry Lorem Ipsum is simply dummy text of the printing.</p>
    <div class="stars">★★★★★</div>
  </div>
  <svg class="abs" style="left:702px;top:2565px" width="18" height="16" viewBox="0 0 18 16"><path d="M2 14 L6 2 H9 L7 14 Z M10 14 L14 2 H17 L15 14 Z" fill="#1f1f1f"/></svg>
  <svg class="abs" style="left:955px;top:2565px" width="18" height="16" viewBox="0 0 18 16"><path d="M2 14 L6 2 H9 L7 14 Z M10 14 L14 2 H17 L15 14 Z" fill="#1f1f1f"/></svg>
  <div class="abs" style="left:803px;top:2620px;display:flex;gap:7px"><span style="width:9px;height:9px;border-radius:50%;background:var(--blue)"></span><span style="width:9px;height:9px;border-radius:50%;background:#aaa"></span><span style="width:9px;height:9px;border-radius:50%;background:#aaa"></span></div>
  <div class="btn" style="left:525px;top:2724px;width:150px;height:34px">View More</div>

  <!-- benefits -->
  <section class="benefits-band"></section>
  <div class="photo" style="left:594px;top:2841px;width:486px;height:414px;background:linear-gradient(140deg,#f3f4f6,#c9ced4 40%,#6f7d96 65%,#e0e2e5)" role="img" aria-label="Pliers and stripped wires resting on building plans"></div>
  <div class="benefits-copy">
    <h2>Benefits of Electrician</h2>
    <h3>Fast Election Services</h3>
    <p>Lorem Ipsum is simply dummy text of the printing and type setting industry. Lorem Ipsum has been the industry's stand ard dummy text ever since the 1500s</p>
    <p>when an unknown printer took a galley of type and scrambled it to make a type specimen book.</p>
  </div>
  <div class="btn dark" style="left:118px;top:3133px;width:148px;height:32px">Read More</div>

  <!-- blog -->
  <h2 class="section-title" style="top:3327px;font-size:23px">OUR BLOGS</h2>
  <p class="section-sub" style="top:3360px;font-weight:400;font-size:14px">Lorem Ipsum is simply dummy text.</p>

  <article class="post" style="left:99px">
    <div class="thumb" style="background:linear-gradient(135deg,#d7d9dc,#c24b3a 40%,#3b72b5 70%,#cfd2d5)" role="img" aria-label="Hands wiring a circuit board"><div class="date-badge">01<br>Nov</div></div>
    <h4>Office Post Title</h4>
    <div class="meta"><span>February 01, 2018</span><span>20</span><span>12</span></div>
    <p>Lorem Ipsum is simply dummy text of the And printing matter and typesetting industry.</p>
    <div class="more">Read More...</div>
  </article>
  <article class="post" style="left:444px">
    <div class="thumb" style="background:linear-gradient(135deg,#eef0f2,#7f98b3 45%,#394e66)" role="img" aria-label="Electrician testing a switchboard"><div class="date-badge">01<br>Nov</div></div>
    <h4>Office Post Title</h4>
    <div class="meta"><span>February 04, 2018</span><span>20</span><span>12</span></div>
    <p>Lorem Ipsum is simply dummy text of the printing and typesetting industry.</p>
    <div class="more">Read More...</div>
  </article>
  <article class="post" style="left:780px">
    <div class="thumb" style="background:linear-gradient(135deg,#f2f2f2,#c9a17f 40%,#7d8a98 75%)" role="img" aria-label="Hands connecting wires to a socket"><div class="date-badge">01<br>Nov</div></div>
    <h4>House Post Title</h4>
    <div class="meta"><span>February 07, 2018</span><span>20</span><span>12</span></div>
    <p>Lorem Ipsum is simply dummy text of the printing and typesetting industry.</p>
    <div class="more">Read More...</div>
  </article>

  <div class="btn" style="left:525px;top:3801px;width:150px;height:34px">View More</div>

  <!-- newsletter -->
  <h2 class="section-title" style="top:3906px;font-size:21px">JOIN OUR NEWSLETTER</h2>
  <p class="section-sub" style="top:3938px;font-weight:400;font-size:14px">Sign up for Our Newsletter</p>
  <div class="news-input">Email Here</div>
  <div class="btn news-btn">SUBSCRIBE</div>

  <!-- footer -->
  <footer class="site-footer">
    <div class="footer-col" style="left:115px;top:40px;width:230px">
      <div style="display:flex;align-items:center;gap:10px;margin-bottom:14px">
        <span style="width:30px;height:30px;border-radius:50%;background:var(--white)"></span>
        <span style="font-family:Montserrat,Arial,sans-serif;font-weight:600;font-size:16px;color:var(--white);line-height:1.2">RTV ELECTRICAL<br>GROUP</span>
      </div>
      <p style="font-size:13.5px;line-height:1.35">Lorem Ipsum is simply dummy of the printing and typesetting Industry.</p>
      <div class="social"><span></span><span></span><span></span><span></span><span></span></div>
    </div>
    <div class="footer-col" style="left:395px">
      <h4>QUICK LINK</h4>
      <ul><li>HOME</li><li>ABOUT US</li><li>SERVICES</li><li>PROJECT GALLERY</li><li>BLOG</li><li>CONTACT</li></ul>
    </div>
    <div class="footer-col" style="left:576px;width:215px">
      <h4>ADDRESS</h4>
      <div class="addr-row"><span class="pin"></span><span>100 Example Street, Sydney<br>NSW 2000, Australia</span></div>
      <div class="addr-row"><span class="pin"></span><span>0491 570 156</span></div>
      <div class="addr-row"><span class="pin"></span><span>(02) 5550 4821</span></div>
      <div class="addr-row" style="font-size:12px"><span class="pin"></span><span>info@rtvelectrical.example.com.au</span></div>
    </div>
    <div class="footer-col" style="left:805px;width:275px">
      <h4>QUICK CONTACT</h4>
      <div style="display:flex;gap:8px;margin-bottom:8px"><div class="mini-field" style="flex:1">Name</div><div class="mini-field" style="flex:1">Phone</div></div>
      <div class="mini-field" style="height:56px">Message</div>
      <div style="margin:10px 0 0 125px;width:150px;height:30px;background:var(--blue);color:#fff;font-weight:700;font-size:13px;display:flex;align-items:center;justify-content:center;border-radius:3px">SEND</div>
    </div>
  </footer>
  <div class="copyright">Copyright © 2018 RTV ELECTRICAL GROUP.  All Rights Reserved.</div>
  <div class="live-chat"><i></i>Live Chat</div>

</div>
</body>
</html>
```